Post Surgery Care Reminder App

Mobile app-based reminder for patients after surgery. Often times once the patient goes home, they are instructed to take medications and perform other care for their wounds. This app will be designed to help patients keep on top of their care to ensure optimal outcomes after their surgery. See the attached video link (clipnest) in the "Must Haves" section for example of our current beta version.

We have immediate room for improvements from the version in the video; looking for designer/coder to help us complete this project to move to consumers.

Target Market(s)

Patients undergoing elective surgeries

Industry/Entity Type

Health Care

Colors

Designer to choose colors to be used in the design.

Requirements
Must have
• Please see linked clipnest video for demonstration:
• https://www.clipnest.com/watch?v=pRaKe7Wq2bN
Nice to have
• Improved user interface: pleasing to the eye as well as smooth and easy to navigate experience.

```html
<!DOCTYPE html>
<html lang="en">
<head>
<meta charset="utf-8">
<title>Remind me to strip my drains</title>
<link rel="stylesheet" href="https://fonts.googleapis.com/css2?family=Roboto:wght@400;500&family=Arimo:wght@400&display=swap">
<style>
:root{
  --page-bg:#e8f4f6;
  --status-blue:#0070c4;
  --screen-bg:#f3f4f9;
  --field-bg:#ffffff;
  --title-ink:#3b404b;
  --field-ink:#6b7280;
  --label-ink:#454a54;
  --icon-ink:#707680;
  --btn-green:#13c296;
  --btn-teal:#00a3c4;
  --alarm-red:#d7262b;
  --radio-blue:#4ab8e8;
  --kb-bg:#d0d4da;
  --key-bg:#ffffff;
  --key-dark:#abb1ba;
  --key-ink:#111111;
}
*{box-sizing:border-box;margin:0;padding:0}
html,body{width:1200px;height:1200px;overflow:hidden;background:var(--page-bg)}
.screen{
  position:absolute;left:271px;top:14px;width:576px;height:1027px;
  transform:scale(1.14);transform-origin:top left;
  background:var(--screen-bg);font-family:"Roboto",sans-serif;overflow:hidden;
}
.status-bar{position:absolute;left:0;top:0;width:100%;height:38px;background:var(--status-blue);
  display:flex;align-items:center;justify-content:flex-end;gap:8px;padding-right:12px;color:#fff;font-size:21px}
.app-header{position:absolute;left:0;top:60px;width:100%;height:48px}
.back-arrow{position:absolute;left:22px;top:11px}
.screen-title{position:absolute;left:96px;top:4px;font-size:28px;font-weight:500;color:var(--title-ink)}
.field{position:absolute;left:22px;width:531px;height:67px;background:var(--field-bg);
  box-shadow:0 1px 3px rgba(0,0,0,.06);display:flex;align-items:center;font-size:22px;color:var(--field-ink)}
.field .lead-icon{position:absolute;left:22px;top:21px}
.field .label{position:absolute;left:71px}
.field-id{top:220px}.field-date{top:300px}.field-time{top:380px}
.trail-cal{position:absolute;right:20px;top:19px}
.alarm-clock{position:absolute;left:232px;top:15px}
.radio{position:absolute;left:336px;top:21px;width:26px;height:26px;border-radius:50%;background:#e3f3fb;display:flex;align-items:center;justify-content:center}
.radio::after{content:"";width:12px;height:12px;border-radius:50%;background:var(--radio-blue)}
.initial-label{position:absolute;left:382px;top:17px;color:var(--label-ink)}
.btn{position:absolute;top:484px;width:256px;height:66px;color:#fff;font-size:23px;font-weight:500;
  display:flex;align-items:center;justify-content:center;border-radius:2px}
.btn-add{left:22px;background:var(--btn-green)}
.btn-create{left:297px;background:var(--btn-teal)}
.keyboard{position:absolute;left:0;top:636px;width:100%;height:391px;background:var(--kb-bg);font-family:"Arimo",sans-serif}
.key{position:absolute;width:46px;height:68px;background:var(--key-bg);border-radius:7px;
  box-shadow:0 2px 0 #8e949c;display:flex;align-items:center;justify-content:center;font-size:37px;color:var(--key-ink)}
.key.dark{background:var(--key-dark)}
.key.small{font-size:27px}
</style>
</head>
<body>
<main class="screen">
  <div class="status-bar">
    <svg width="30" height="22" viewBox="0 0 30 22"><path d="M0 4 Q15 -4 30 4 L15 22Z" fill="#fff"/></svg>
    <svg width="22" height="22" viewBox="0 0 22 22"><path d="M22 0 V22 H0Z" fill="#fff"/></svg>
    <svg width="14" height="22" viewBox="0 0 14 22"><rect x="4" y="0" width="6" height="3" fill="#fff"/><rect x="0" y="2" width="14" height="20" rx="1" fill="#fff"/></svg>
    <span>12:30</span>
  </div>

  <header class="app-header">
    <svg class="back-arrow" width="28" height="26" viewBox="0 0 28 26"><path d="M27 13H3M13 3L3 13l10 10" fill="none" stroke="#4a4f58" stroke-width="2"/></svg>
    <h1 class="screen-title">Remind me to strip my drains</h1>
  </header>

  <div class="field field-id">
    <svg class="lead-icon" width="26" height="26" viewBox="0 0 26 26"><path d="M4 22 L6 15 L18 3 L23 8 L11 20Z M3 24 H24" fill="none" stroke="var(--icon-ink)" stroke-width="1.6"/></svg>
    <span class="label">Enter an ID</span>
  </div>

  <div class="field field-date">
    <svg class="lead-icon" width="26" height="26" viewBox="0 0 26 26"><rect x="2" y="4" width="22" height="20" fill="none" stroke="var(--icon-ink)" stroke-width="1.6"/><path d="M2 9H24M7 2V6M19 2V6" stroke="var(--icon-ink)" stroke-width="1.6"/><g fill="var(--icon-ink)"><rect x="6" y="12" width="2" height="2"/><rect x="10" y="12" width="2" height="2"/><rect x="14" y="12" width="2" height="2"/><rect x="18" y="12" width="2" height="2"/><rect x="6" y="17" width="2" height="2"/><rect x="10" y="17" width="2" height="2"/><rect x="14" y="17" width="2" height="2"/></g></svg>
    <span class="label">Select Date</span>
    <svg class="trail-cal" width="30" height="30" viewBox="0 0 30 30"><rect x="1" y="4" width="28" height="25" rx="2" fill="#e6e8ec"/><rect x="1" y="4" width="28" height="8" rx="2" fill="#e8413b"/><rect x="7" y="1" width="3" height="6" fill="#8a8f98"/><rect x="20" y="1" width="3" height="6" fill="#8a8f98"/><g fill="#9aa0a8"><rect x="6" y="15" width="3" height="3"/><rect x="11" y="15" width="3" height="3"/><rect x="16" y="15" width="3" height="3"/><rect x="21" y="15" width="3" height="3"/><rect x="6" y="21" width="3" height="3"/><rect x="11" y="21" width="3" height="3"/><rect x="16" y="21" width="3" height="3"/><rect x="21" y="21" width="3" height="3"/></g></svg>
  </div>

  <div class="field field-time">
    <svg class="lead-icon" width="26" height="26" viewBox="0 0 26 26"><circle cx="13" cy="13" r="11.5" fill="none" stroke="var(--icon-ink)" stroke-width="1.6"/><path d="M13 6V13H19" fill="none" stroke="var(--icon-ink)" stroke-width="1.6"/></svg>
    <span class="label">Select Time</span>
    <svg class="alarm-clock" width="36" height="36" viewBox="0 0 36 36"><path d="M3 9 Q4 2 11 3Z M33 9 Q32 2 25 3Z" fill="#333"/><circle cx="18" cy="19" r="13" fill="#fff" stroke="var(--alarm-red)" stroke-width="3"/><path d="M18 10V19L23 23" fill="none" stroke="#333" stroke-width="1.8"/><path d="M8 33L11 29M28 33L25 29" stroke="#333" stroke-width="2"/></svg>
    <span class="radio"></span>
    <span class="initial-label">Initial Alarm</span>
  </div>

  <div class="btn btn-add">Add Another Alarm</div>
  <div class="btn btn-create">Create Alarm</div>

  <section class="keyboard">
    <div class="key" style="left:5px;top:22px">Q</div>
    <div class="key" style="left:63px;top:22px">W</div>
    <div class="key" style="left:121px;top:22px">E</div>
    <div class="key" style="left:179px;top:22px">R</div>
    <div class="key" style="left:237px;top:22px">T</div>
    <div class="key" style="left:295px;top:22px">Y</div>
    <div class="key" style="left:353px;top:22px">U</div>
    <div class="key" style="left:411px;top:22px">I</div>
    <div class="key" style="left:469px;top:22px">O</div>
    <div class="key" style="left:527px;top:22px">P</div>

    <div class="key" style="left:34px;top:119px">A</div>
    <div class="key" style="left:92px;top:119px">S</div>
    <div class="key" style="left:150px;top:119px">D</div>
    <div class="key" style="left:208px;top:119px">F</div>
    <div class="key" style="left:266px;top:119px">G</div>
    <div class="key" style="left:324px;top:119px">H</div>
    <div class="key" style="left:382px;top:119px">J</div>
    <div class="key" style="left:440px;top:119px">K</div>
    <div class="key" style="left:498px;top:119px">L</div>

    <div class="key" style="left:5px;top:216px;width:65px">
      <svg width="34" height="30" viewBox="0 0 34 30"><path d="M17 1 L33 17 H24 V29 H10 V17 H1Z" fill="#111"/></svg>
    </div>
    <div class="key" style="left:92px;top:216px">Z</div>
    <div class="key" style="left:150px;top:216px">X</div>
    <div class="key" style="left:208px;top:216px">C</div>
    <div class="key" style="left:266px;top:216px">V</div>
    <div class="key" style="left:324px;top:216px">B</div>
    <div class="key" style="left:382px;top:216px">N</div>
    <div class="key" style="left:440px;top:216px">M</div>
    <div class="key dark" style="left:506px;top:216px;width:64px">
      <svg width="40" height="28" viewBox="0 0 40 28"><path d="M12 1 H38 V27 H12 L1 14Z" fill="#fff"/><path d="M20 8L30 20M30 8L20 20" stroke="#9aa0a8" stroke-width="2"/></svg>
    </div>

    <div class="key dark small" style="left:5px;top:314px;width:61px">123</div>
    <div class="key dark" style="left:77px;top:314px;width:60px">
      <svg width="36" height="36" viewBox="0 0 36 36" fill="none" stroke="#222" stroke-width="1.6"><circle cx="18" cy="18" r="16"/><ellipse cx="18" cy="18" rx="7" ry="16"/><path d="M2 18H34M5 10H31M5 26H31M18 2V34"/></svg>
    </div>
    <div class="key" style="left:149px;top:314px">
      <svg width="22" height="36" viewBox="0 0 22 36" fill="none" stroke="#222" stroke-width="1.8"><rect x="6" y="2" width="10" height="20" rx="5"/><path d="M2 16Q2 28 11 28Q20 28 20 16M11 28V34"/></svg>
    </div>
    <div class="key small" style="left:207px;top:314px;width:219px">space</div>
    <div class="key dark small" style="left:438px;top:314px;width:132px;color:#7b8089">Search</div>
  </section>
</main>
</body>
</html>
```